Website redesign

We need a bold revamp of our website (http://www.brantwoodpower.co.nz/)
which at the moment looks dated. We want a crisp, fresh and bold look. The background image behind web page can go. Open to complete new layout

Target Market(s)

Electrical contracting company- working in the domestic and commercial field

Coding

Coded - Design and coding required

Number of Pages Required

5+ page

Font styles to use
Sans Serif

Colors

Designer to choose colors to be used in the design.

```html
<!DOCTYPE html>
<html lang="en">
<head>
<meta charset="utf-8">
<title>Brantwood Power – Electrical Contractors</title>
<link href="https://fonts.googleapis.com/css2?family=Lato:ital,wght@0,400;0,700;0,900;1,400;1,700&family=Montserrat:wght@600;700&display=swap" rel="stylesheet">
<style>
:root{
  --red:#e4121b;
  --red-dark:#c40d15;
  --ink:#1b1b1b;
  --text:#444;
  --muted:#666;
  --light:#eeeef1;
  --dark:#151515;
  --white:#fff;
  --purple:#4b3a78;
}
*{box-sizing:border-box;margin:0;padding:0}
html,body{width:1200px;height:4225px;overflow:hidden}
body{font-family:'Lato',sans-serif;color:var(--text);background:var(--white);font-size:14px;line-height:1.55}
a{color:inherit;text-decoration:none}

/* header */
.site-header{position:relative;height:143px}
.topbar{position:absolute;right:0;top:0;width:450px;height:32px;background:var(--dark);border-bottom-left-radius:20px;color:var(--white);font-size:15px;font-weight:700;display:flex;align-items:center;justify-content:center;gap:8px}
.topbar .call{color:var(--red)}
.brand{position:absolute;left:66px;top:58px;display:flex;align-items:center;gap:12px;font-family:'Lato',sans-serif;font-weight:900;font-size:34px;color:var(--ink);letter-spacing:.5px}
.brand .mark{width:30px;height:30px;background:var(--red)}
.follow{position:absolute;right:215px;top:74px;display:flex;align-items:center;gap:6px;color:var(--red);font-weight:900;font-size:21px}
.follow span{margin-right:8px}
.dot{width:22px;height:22px;border-radius:50%;background:var(--ink);display:inline-block}
.local-badge{position:absolute;right:58px;top:112px;width:74px;height:74px;border-radius:50%;background:#f2f2f2;border:6px solid #7cc242;z-index:3}

.main-nav{height:35px;background:var(--red);display:flex;padding-left:68px}
.main-nav a{width:128px;border-right:1px solid var(--red-dark);color:var(--white);font-size:15px;display:flex;align-items:center;justify-content:center}
.main-nav a.active{background:var(--dark);width:108px}

/* hero */
.hero{position:relative;height:622px;background:linear-gradient(135deg,#f4f4f4 0%,#bdbdbd 35%,#6e6e6e 60%,#d0d0d0 100%)}
.hero-panel{position:absolute;left:68px;right:70px;top:358px;height:264px;background:rgba(235,235,238,.78);border-radius:18px 18px 0 0;text-align:center;padding-top:60px}
.hero-panel h1{font-family:'Montserrat',sans-serif;color:var(--red);font-size:50px;font-weight:700;letter-spacing:1px}
.hero-panel p{width:560px;margin:14px auto 0;font-size:13px;font-weight:700;color:var(--ink);line-height:1.6}
.arrow{position:absolute;top:486px;width:36px;height:36px;background:var(--white);display:flex;align-items:center;justify-content:center}
.arrow.prev{left:96px}.arrow.next{right:96px}

/* services grid */
.service-grid{height:675px;background:var(--light);padding:65px 0 0 68px;display:grid;grid-template-columns:repeat(3,344px);grid-auto-rows:191px;column-gap:18px;row-gap:16px}
.service-card{background:var(--white);border:2px solid #2b2b2b;position:relative}
.service-card .thumb{height:78px;position:relative}
.service-card .label{position:absolute;left:0;right:0;bottom:0;height:30px;background:rgba(20,20,20,.75);color:var(--white);font-size:24px;line-height:30px;padding-left:6px;letter-spacing:.5px}
.service-card p{font-size:13px;padding:24px 10px 0;color:var(--text)}
.service-card .more{position:absolute;right:10px;bottom:10px;font-size:12px;color:var(--ink)}
.service-card .more b{color:var(--red)}

/* section heading */
.section-title{display:flex;align-items:center;gap:12px;font-family:'Montserrat',sans-serif;font-weight:700;font-size:33px;color:var(--ink)}
.section-title .mark{width:28px;height:28px;background:var(--red)}
.section-title.center{justify-content:center}
.rule{width:48px;height:3px;background:var(--ink);margin:26px auto 0}

/* about */
.about{position:relative;height:895px;padding:175px 0 0 68px}
.about .tagline{color:var(--red);font-style:italic;font-weight:700;font-size:18px;margin:22px 0 18px}
.about p{font-size:14.5px;color:var(--text);margin-bottom:20px;width:1060px}
.about p.narrow{width:630px}
.about-photo{position:absolute;left:721px;top:167px;width:408px;height:325px;border:1px solid #ccc;background:linear-gradient(135deg,#e8eef6,#b9c7d8 55%,#7d8ea4)}
.btn-dark{display:inline-block;background:var(--dark);color:var(--red);font-size:11px;width:136px;height:38px;line-height:38px;text-align:center;margin-top:28px}

/* our services band */
.services-band{height:436px;background:linear-gradient(90deg,#0c0c0c,#2a2a2c 50%,#0c0c0c);text-align:center;color:var(--white);padding-top:88px}
.services-band .section-title{color:var(--white)}
.services-band .rule{background:var(--white)}
.services-band p{width:700px;margin:26px auto 0;font-size:14px;line-height:1.6}
.services-band p+p{margin-top:18px}
.btn-light{display:inline-block;background:var(--white);color:var(--ink);font-size:12px;width:136px;height:40px;line-height:40px;margin-top:24px}

/* projects */
.projects{height:600px;padding-top:78px}
.project-list{display:grid;grid-template-columns:560px 560px;column-gap:10px;row-gap:56px;margin:54px 0 0 68px}
.project{display:flex;gap:30px}
.project .thumb{width:126px;height:120px;flex:none;margin-top:8px}
.project:nth-child(even){margin-top:-14px}
.project:nth-child(even) .thumb{width:128px;height:112px}
.project h3{color:var(--red);font-size:15px;font-weight:700;margin-bottom:14px}
.project p{font-size:13.5px;color:var(--text);width:300px}
.project .more{font-size:12px;color:var(--ink);display:block;margin-top:12px}
.project .more b{color:var(--red)}

/* testimonial */
.testimonial{position:relative;height:442px;background:linear-gradient(180deg,#3a2f67 0%,#5a4a8c 55%,#8a7bb3 100%);text-align:center;color:var(--white);padding-top:66px}
.testimonial .glow{position:absolute;right:0;top:110px;width:300px;height:332px;background:radial-gradient(circle at 70% 50%,rgba(255,240,200,.85),rgba(255,200,150,.25) 45%,transparent 70%)}
.testimonial .quote-mark{color:var(--red);font-size:70px;font-weight:900;line-height:1;height:46px;font-family:'Montserrat',sans-serif}
.testimonial blockquote{width:600px;margin:12px auto 0;font-style:italic;font-size:14px;line-height:1.6}
.avatar{width:100px;height:100px;border-radius:50%;border:4px solid var(--white);background:linear-gradient(135deg,#d9d0c4,#9a8a7a);margin:28px auto 8px}
.person{color:var(--red);font-weight:700;font-size:14px}
.person-role{font-size:11px;line-height:1.3}
.dots{display:flex;gap:10px;justify-content:center;margin-top:16px}
.dots i{width:12px;height:12px;border-radius:50%;background:var(--white)}
.dots i:first-child{background:var(--red)}

/* footer */
.site-footer{height:310px;background:var(--red);color:var(--white);display:flex;padding-top:52px}
.footer-col{border-right:1px solid rgba(255,255,255,.6);padding:0 0 0 28px;height:206px}
.footer-col:last-child{border:none}
.footer-col h4{font-family:'Montserrat',sans-serif;font-weight:600;font-size:21px;letter-spacing:1px;margin-bottom:20px}
.col-brand{width:296px;padding-left:68px}
.col-brand .f-brand{font-weight:900;font-size:28px;line-height:1.1}
.col-brand p{font-size:12px;margin-top:18px;line-height:1.4}
.col-partners{width:212px}
.col-partners .lead{font-weight:900;font-size:19px;line-height:1.15}
.badge{background:var(--white);border-radius:4px;margin-top:10px}
.col-links{width:214px}
.col-links li{list-style:none;font-size:16px;margin-bottom:6px}
.col-links li::before{content:"›";margin-right:10px}
.col-contact{width:218px;font-size:12px}
.col-contact .row{display:flex;align-items:center;gap:8px;margin-bottom:8px}
.col-contact svg{flex:none}
.col-follow{width:260px}
.col-follow .dot{background:var(--white);width:26px;height:26px;margin-right:4px}
.col-follow .call-us{font-family:'Montserrat',sans-serif;font-size:18px;margin-top:28px;letter-spacing:1px}
.col-follow .num{font-size:25px;font-weight:700;line-height:1.2}

.copyright{height:65px;background:var(--dark);color:#ccc;font-size:15px;display:flex;align-items:center;justify-content:center;gap:6px}
.copyright .hl{color:var(--red)}
</style>
</head>
<body>

<header class="site-header">
  <div class="topbar"><span class="call">Call us Free</span><span>0800 55 01 20 | (06) 555 0142</span></div>
  <a class="brand" href="#"><span class="mark"></span>Brantwood Power</a>
  <div class="follow"><span>Follow Us</span><i class="dot"></i><i class="dot"></i><i class="dot"></i><i class="dot"></i></div>
  <div class="local-badge" role="img" aria-label="Local business badge"></div>
</header>

<nav class="main-nav">
  <a class="active" href="#">Home</a><a href="#">About us</a><a href="#">Services</a><a href="#">Projects</a><a href="#">Contact us</a><a href="#">Info</a>
</nav>

<section class="hero" role="img" aria-label="Network cabling and patch panel photograph">
  <div class="hero-panel">
    <h1>LOREM IPSUM</h1>
    <p>Lorem ipsum dolor sit amet, consectetur adipiscing elit. Quid autem habent admirationis, prope accesseris. Lorem ipsum dolor sit amet, consectetur adipiscing elit. Lorem ipsum dolor sit amet, consectetur adipiscing elit.</p>
  </div>
  <a class="arrow prev" href="#"><svg width="14" height="20" viewBox="0 0 14 20"><path d="M11 2 3 10l8 8" fill="none" stroke="#111" stroke-width="3"/></svg></a>
  <a class="arrow next" href="#"><svg width="14" height="20" viewBox="0 0 14 20"><path d="M3 2l8 8-8 8" fill="none" stroke="#111" stroke-width="3"/></svg></a>
</section>

<section class="service-grid">
  <article class="service-card"><div class="thumb" role="img" aria-label="Electrician working on wiring" style="background:linear-gradient(90deg,#c9c2b8,#8a3b2a 60%,#d6513a)"><span class="label">Electrical</span></div><p>Lorem ipsum dolor sit amet, consectetur adipiscing elit. Quid autem habent admirationis.</p><a class="more" href="#">Read more <b>»</b></a></article>
  <article class="service-card"><div class="thumb" role="img" aria-label="Appliance testing equipment" style="background:linear-gradient(90deg,#ddd,#8a8a8a 55%,#c9c9c9)"><span class="label">Appliance Testing</span></div><p>Lorem ipsum dolor sit amet, consectetur adipiscing elit. Quid autem habent admirationis.</p><a class="more" href="#">Read more <b>»</b></a></article>
  <article class="service-card"><div class="thumb" role="img" aria-label="Alarm keypad" style="background:linear-gradient(90deg,#6f8a6a,#cfd6cc 60%,#9fb09a)"><span class="label">Alarms</span></div><p>Lorem ipsum dolor sit amet, consectetur adipiscing elit. Quid autem habent admirationis.</p><a class="more" href="#">Read more <b>»</b></a></article>
  <article class="service-card"><div class="thumb" role="img" aria-label="Security cameras on a wall" style="background:linear-gradient(90deg,#4f7fb8,#a9c3e0 60%,#6f96c6)"><span class="label">Security Cameras</span></div><p>Lorem ipsum dolor sit amet, consectetur adipiscing elit. Quid autem habent admirationis.</p><a class="more" href="#">Read more <b>»</b></a></article>
  <article class="service-card"><div class="thumb" role="img" aria-label="Heat pump unit" style="background:linear-gradient(90deg,#f1f1f1,#bfc4c8 60%,#e6e6e6)"><span class="label">Heat Pumps</span></div><p>Lorem ipsum dolor sit amet, consectetur adipiscing elit. Quid autem habent admirationis.</p><a class="more" href="#">Read more <b>»</b></a></article>
  <article class="service-card"><div class="thumb" role="img" aria-label="Fire alarm and smoke detector" style="background:linear-gradient(90deg,#d8d2c8,#b33a2e 55%,#e3ddd3)"><span class="label">Fire/Smoke</span></div><p>Lorem ipsum dolor sit amet, consectetur adipiscing elit. Quid autem habent admirationis.</p><a class="more" href="#">Read more <b>»</b></a></article>
  <article class="service-card"><div class="thumb" role="img" aria-label="Building compliance inspection" style="background:linear-gradient(90deg,#3b4a5a,#7d8b98 60%,#4a5866)"><span class="label">IQP Building Compliance</span></div><p>Lorem ipsum dolor sit amet, consectetur adipiscing elit. Quid autem habent admirationis.</p><a class="more" href="#">Read more <b>»</b></a></article>
  <article class="service-card"><div class="thumb" role="img" aria-label="Data cabling and phone lines" style="background:linear-gradient(90deg,#2e5e8a,#6fa2c9 55%,#1e3e5e)"><span class="label">Phone/Data</span></div><p>Lorem ipsum dolor sit amet, consectetur adipiscing elit. Quid autem habent admirationis.</p><a class="more" href="#">Read more <b>»</b></a></article>
  <article class="service-card"><div class="thumb" role="img" aria-label="Satellite dish and aerial" style="background:linear-gradient(90deg,#7aa6d6,#c8dcef 60%,#8cb3dc)"><span class="label">TV - Satellite/Aerial</span></div><p>Lorem ipsum dolor sit amet, consectetur adipiscing elit. Quid autem habent admirationis.</p><a class="more" href="#">Read more <b>»</b></a></article>
</section>

<section class="about">
  <h2 class="section-title"><span class="mark"></span>ABOUT US</h2>
  <p class="tagline">Proudly serving our local community for over 20 years</p>
  <p class="narrow">Brantwood Power is a leading electrical installation and maintenance company based in Riverton, but servicing all New Zealand. We are proud to be locally owned and operated. With over 15 employees, we are a very professional qualified and experienced team of technicians and support staff.</p>
  <p class="narrow">Brantwood Power was established in 1991 and does it all, from supplying and changing light bulbs, comprehensive whole house electrical design and installation, to commercial and large scale industrial consultation, implementation and servicing.</p>
  <p>With over 20 years' experience in providing our customers with personalized service for their home electrical needs, individual lighting plans, experienced advise on renovations, heating and cooling requirements for home comfort, security systems and cameras, and providing the most up to date equipment and knowledge of energy efficiency and all electrical legislation.</p>
  <p>As Riverton's top Kaizen Air accredited installers and Riverton's ONLY member of The Climate Installers Guild of New Zealand (CIG) we aim to continue to provide the Riverton region with the highest possible quality of professional service.</p>
  <p>Our goal is to provide you with the best possible electrical advice and service. In everything we do, from consultation and design to finishing the job, our commitment to providing reliable, high quality services is evident. Our electrical technicians are on call 24 hour, 7 days a week.</p>
  <p>Let us provide the peace of mind that comes with knowing that all workmanship is guaranteed and done to meet all the regulations and standards with integrity, experience and dedication.</p>
  <a class="btn-dark" href="#">READ MORE</a>
  <div class="about-photo" role="img" aria-label="Electrician in a hard hat working on a switchboard"></div>
</section>

<section class="services-band">
  <h2 class="section-title center"><span class="mark"></span>OUR SERVICES</h2>
  <div class="rule"></div>
  <p>Brantwood Power offers all the domestic and commercial electrical services you would expect from an electrical firm, but with dedicated technicians in specialist electrical areas they have the more technical ability and experience than your average sparky.</p>
  <p>If you can't find what you are looking for in the appropriate sections listed, simply contact us on 0800 55 01 20 and we will be able to help you out.</p>
  <a class="btn-light" href="#">READ MORE</a>
</section>

<section class="projects">
  <h2 class="section-title center"><span class="mark"></span>OUR PROJECTS</h2>
  <div class="rule"></div>
  <div class="project-list">
    <article class="project"><div class="thumb" role="img" aria-label="Commercial building project" style="background:linear-gradient(135deg,#9fb8d4,#3d5f86)"></div><div><h3>Lorem ipsum dolor sit amet</h3><p>Lorem ipsum dolor sit amet, consectetur adipiscing elit. Quid autem habent admirationis,prope accesseris. Lorem ipsum dolor sit amet, consectetur adipiscing elit.</p><a class="more" href="#">Read more <b>»</b></a></div></article>
    <article class="project"><div class="thumb" role="img" aria-label="Technician installing equipment" style="background:linear-gradient(135deg,#d0d6de,#5d6f86)"></div><div><h3>Lorem ipsum dolor sit amet</h3><p>Lorem ipsum dolor sit amet, consectetur adipiscing elit. Quid autem habent admirationis,prope accesseris. Lorem ipsum dolor sit amet, consectetur adipiscing elit.</p><a class="more" href="#">Read more <b>»</b></a></div></article>
    <article class="project"><div class="thumb" role="img" aria-label="Switchboard wiring" style="background:linear-gradient(135deg,#c8c0a0,#3f4a5a)"></div><div><h3>Lorem ipsum dolor sit amet</h3><p>Lorem ipsum dolor sit amet, consectetur adipiscing elit. Quid autem habent admirationis,prope accesseris. Lorem ipsum dolor sit amet, consectetur adipiscing elit.</p><a class="more" href="#">Read more <b>»</b></a></div></article>
    <article class="project"><div class="thumb" role="img" aria-label="Heat pump installation" style="background:linear-gradient(135deg,#f2f4f7,#a8b6c6)"></div><div><h3>Lorem ipsum dolor sit amet</h3><p>Lorem ipsum dolor sit amet, consectetur adipiscing elit. Quid autem habent admirationis,prope accesseris. Lorem ipsum dolor sit amet, consectetur adipiscing elit.</p><a class="more" href="#">Read more <b>»</b></a></div></article>
  </div>
</section>

<section class="testimonial">
  <div class="glow" role="img" aria-label="Glowing light bulb"></div>
  <div class="quote-mark">“</div>
  <blockquote>Lorem ipsum dolor sit amet, consectetur adipiscing elit. Quid autem habent admirationis, cum prope accesseris? Lorem ipsum dolor sit amet, consectetur adipiscing elit. Quid autem habent admirations, cum prope accesseris?</blockquote>
  <div class="avatar" role="img" aria-label="Customer portrait"></div>
  <div class="person">Sam Carter</div>
  <div class="person-role">Sales manager at Harbourline Freight<br>President at Coastline NP</div>
  <div class="dots"><i></i><i></i><i></i><i></i></div>
</section>

<footer class="site-footer">
  <div class="footer-col col-brand">
    <div class="f-brand">Brantwood Power</div>
    <p>Lorem ipsum dolor sit amet, consectetur adipiscing elit. Quid autem habent admirationis, cum prope accesseris</p>
  </div>
  <div class="footer-col col-partners">
    <div class="lead">We are authorised installers for:</div>
    <div class="badge" style="width:116px;height:46px"></div>
    <div class="badge" style="width:96px;height:40px"></div>
  </div>
  <div class="footer-col col-links">
    <h4>QUICK LINKS</h4>
    <ul><li>Home</li><li>About us</li><li>Services</li><li>Projects</li><li>Contact us</li></ul>
  </div>
  <div class="footer-col col-contact">
    <h4>CONTACT</h4>
    <div class="row"><svg width="12" height="16" viewBox="0 0 12 16"><path d="M6 0a6 6 0 0 0-6 6c0 4.5 6 10 6 10s6-5.5 6-10a6 6 0 0 0-6-6zm0 8.5A2.5 2.5 0 1 1 6 3.5a2.5 2.5 0 0 1 0 5z" fill="#fff"/></svg><span>12 Harbour Road,<br>Riverton 4500</span></div>
    <div class="row"><svg width="14" height="14" viewBox="0 0 14 14"><path d="M3 0l3 3-2 2c1 2 3 4 5 5l2-2 3 3-2 3C6 14 0 8 0 2z" fill="#fff"/></svg><span>0800 55 01 20</span></div>
    <div class="row"><svg width="14" height="14" viewBox="0 0 14 14"><path d="M3 0l3 3-2 2c1 2 3 4 5 5l2-2 3 3-2 3C6 14 0 8 0 2z" fill="#fff"/></svg><span>(06) 555 0142</span></div>
    <div class="row"><svg width="14" height="10" viewBox="0 0 14 10"><rect width="14" height="10" fill="#fff"/><path d="M0 0l7 6 7-6" fill="none" stroke="#e4121b"/></svg><span>office@brantwoodpower.co.nz</span></div>
    <div class="row"><svg width="14" height="14" viewBox="0 0 14 14"><circle cx="7" cy="7" r="6" fill="none" stroke="#fff" stroke-width="1.5"/><path d="M1 7h12M7 1c3 3 3 9 0 12M7 1c-3 3-3 9 0 12" fill="none" stroke="#fff"/></svg><span>www.brantwoodpower.co.nz</span></div>
  </div>
  <div class="footer-col col-follow">
    <h4>FOLLOW US ON</h4>
    <i class="dot"></i><i class="dot"></i><i class="dot"></i><i class="dot"></i>
    <div class="call-us">CALL US ON</div>
    <div class="num">0800 55 01 20</div>
    <div class="num">(06) 555 0142</div>
  </div>
</footer>

<div class="copyright">© 2018 <span class="hl">Brantwood Power</span> | Privacy Policy | User Agreement</div>

</body>
</html>
```